Business Card Design

redesign of card and recreation of logo based on image provided. the business is located in new york so the Brooklyn Bridge figures prominently in the scheme. product should be very clean.

Industry/Entity Type

Real Estate

Contact Information for Business Card

Wendell Ortwick 318 Tamsin Street Brooklyn, New York 11409 wendell@qorvane.com Mobile: 917-555-0143

Colors
cadf82
1b1b1b
ffffff

Requirements
Nice to have
• Brooklyn Bridge

```html
<!DOCTYPE html>
<html lang="en">
<head>
<meta charset="utf-8">
<title>Ortwick &amp; Partners — Business Cards</title>
<link href="https://fonts.googleapis.com/css2?family=Montserrat:wght@300;400;600;700&display=swap" rel="stylesheet">
<style>
  :root {
    --green: #a3b46a;
    --green-light: #cadf82;
    --ink: #1b1b1b;
    --grey: #4d4d4f;
    --paper: #ffffff;
    --backdrop: #ececec;
  }
  html, body {
    margin: 0;
    width: 1200px;
    height: 1004px;
    overflow: hidden;
    background: var(--backdrop);
    font-family: "Montserrat", sans-serif;
  }
  .sheet {
    position: relative;
    width: 1200px;
    height: 1004px;
    display: flex;
    align-items: center;
    justify-content: center;
    gap: 40px;
  }
  .card {
    width: 520px;
    height: 298px;
    background: var(--paper);
    box-shadow: 0 2px 10px rgba(0,0,0,0.08);
    position: relative;
    box-sizing: border-box;
  }
  .card--back {
    display: flex;
    align-items: center;
  }
  .card__brand {
    width: 250px;
    display: flex;
    justify-content: center;
  }
  .card__divider {
    width: 1px;
    height: 180px;
    background: var(--green-light);
  }
  .contact {
    padding-left: 36px;
    color: var(--ink);
    font-size: 12px;
    line-height: 1.55;
  }
  .contact__name {
    color: var(--green);
    font-weight: 700;
    font-size: 17px;
    margin: 0 0 6px;
  }
  .contact__line { margin: 0; }
  .contact__address { margin-top: 14px; }
  .contact__street { font-weight: 700; }
  .wordmark {
    display: flex;
    align-items: center;
    gap: 10px;
    font-weight: 600;
    color: var(--grey);
    letter-spacing: 0.02em;
    text-transform: uppercase;
  }
  .wordmark__square {
    width: 14px;
    height: 14px;
    background: var(--green);
  }
  .wordmark--small { font-size: 15px; }
  .wordmark--large { font-size: 24px; }
  .card--front {
    display: flex;
    align-items: center;
    justify-content: center;
  }
</style>
</head>
<body>
  <main class="sheet">
    <section class="card card--back" aria-label="Business card, contact side">
      <div class="card__brand">
        <div class="wordmark wordmark--small">
          <span class="wordmark__square"></span>
          <span>Ortwick &amp; Partners</span>
        </div>
      </div>
      <div class="card__divider"></div>
      <div class="contact">
        <p class="contact__name">Wendell Ortwick</p>
        <p class="contact__line">11409 wendell@qorvane.com</p>
        <p class="contact__line">917-555-0143</p>
        <div class="contact__address">
          <p class="contact__line contact__street">318 Tamsin Street</p>
          <p class="contact__line">Brooklyn, New York</p>
        </div>
      </div>
    </section>

    <section class="card card--front" aria-label="Business card, logo side">
      <div class="wordmark wordmark--large">
        <span class="wordmark__square"></span>
        <span>Ortwick &amp; Partners</span>
      </div>
    </section>
  </main>
</body>
</html>
```